Business card for Internet Marketing Consultant

Simple - need a nice business card design using the logo elements and colors. Keywords: Progressive, professional, stylish, minimalist. Please use the bc as part of the design.

Info for card:

Gareth Pennick
Internet Marketing Strategist
Phone: (520) 318-6047
Email: gareth@brightcanopy.com
Address: 2915 W. Larkmoor Ave., Ste. 118
Tucson, Arizona 85293

Website: www.brightcanopy.com

Industry/Entity Type

Business

Font styles to use
Sans Serif

```html
<!DOCTYPE html>
<html lang="en">
<head>
<meta charset="utf-8">
<title>Bright Canopy – Business Card</title>
<link rel="stylesheet" href="https://fonts.googleapis.com/css2?family=Arimo:wght@400;700&display=swap">
<style>
  :root {
    --backdrop: #e9e6e2;
    --card-black: #0b0b0d;
    --brand-green: #5fd070;
    --brand-blue: #2f6cd6;
    --band-text: #ffffff;
  }
  * { margin: 0; padding: 0; box-sizing: border-box; }
  html, body {
    width: 1200px; height: 960px; overflow: hidden;
    background: var(--backdrop);
    font-family: "Arimo", Arial, sans-serif;
  }
  .sheet {
    position: relative; width: 1200px; height: 960px;
    display: flex; justify-content: center; align-items: center; gap: 100px;
  }
  .card {
    position: relative; width: 400px; height: 700px;
    background: var(--card-black);
    box-shadow: 0 14px 34px rgba(0,0,0,.28);
    overflow: hidden;
  }
  /* front */
  .card-front .brand-lockup {
    position: absolute; top: 290px; left: 0; right: 0;
    display: flex; align-items: center; justify-content: center; gap: 14px;
  }
  .brand-dot { width: 34px; height: 34px; border-radius: 50%; background: var(--brand-blue); }
  .brand-name {
    color: var(--brand-green); font-weight: 700; font-size: 40px; letter-spacing: -0.5px;
  }
  .card-front .front-url {
    position: absolute; top: 380px; left: 0; right: 0; text-align: center;
    color: var(--brand-green); font-size: 17px;
  }
  /* back */
  .card-back .back-lockup {
    position: absolute; top: 80px; right: 40px;
    display: flex; align-items: center; gap: 10px;
  }
  .card-back .brand-dot { width: 22px; height: 22px; }
  .card-back .brand-name { font-size: 30px; }
  .contact-block {
    position: absolute; right: 40px; text-align: right; color: var(--brand-green);
  }
  .person { top: 200px; }
  .person-name { font-weight: 700; font-size: 24px; text-transform: uppercase; letter-spacing: .3px; }
  .person-title { font-size: 17px; margin-top: 6px; }
  .details { top: 330px; font-size: 17px; line-height: 1.6; }
  .url-band {
    position: absolute; left: 0; right: 0; bottom: 0; height: 112px;
    background: var(--brand-blue);
    display: flex; align-items: center; padding-left: 40px;
  }
  .url-band::before {
    content: ""; position: absolute; left: 0; right: 0; top: -6px; height: 2px;
    background: var(--brand-blue);
  }
  .band-url { color: var(--band-text); font-size: 27px; }
</style>
</head>
<body>
<main class="sheet">
  <section class="card card-front" aria-label="Card front">
    <div class="brand-lockup">
      <span class="brand-dot"></span>
      <span class="brand-name">brightcanopy</span>
    </div>
    <p class="front-url">www.brightcanopy.com</p>
  </section>

  <section class="card card-back" aria-label="Card back">
    <div class="back-lockup">
      <span class="brand-dot"></span>
      <span class="brand-name">brightcanopy</span>
    </div>
    <div class="contact-block person">
      <p class="person-name">Gareth Pennick</p>
      <p class="person-title">Internet Marketing Strategist</p>
    </div>
    <div class="contact-block details">
      <p>(520) 318-6047</p>
      <p>gareth@brightcanopy.com</p>
      <p>2915 W. Larkmoor Ave.</p>
      <p>Ste. 118 Tucson Arizona 85293</p>
    </div>
    <div class="url-band">
      <span class="band-url">www.brightcanopy.com</span>
    </div>
  </section>
</main>
</body>
</html>
```